KRV In Home Flier

To prepare a flier to be placed directly into existing clients homes, which shares additional services available. These are clients that are using KRV Cleaning services and we want to use our KRV Pest Control or BMO (Bravo Mend On)Maintenance Services

Target Market(s)

residential home owners / Renters

Industry/Entity Type

Property Maintenance

Colors

Designer to choose colors to be used in the design.

Requirements
Must have
• Must be crisp and clean - design should pop - A CLEAR call to action
Nice to have
• See previous designed uploaded
Should not have

```html
<!DOCTYPE html>
<html lang="en">
<head>
<meta charset="utf-8">
<title>KRV Pest Control Flier</title>
<link href="https://fonts.googleapis.com/css2?family=Cinzel:wght@400;600;700&family=Lato:wght@400;700&display=swap" rel="stylesheet">
<style>
  :root{
    --stage:#3a3c3f;
    --paper:#ffffff;
    --magenta:#c8307a;
    --magenta-dark:#a82365;
    --blue:#1f6fb8;
    --navy:#0f1d3a;
    --orange:#ef8f12;
    --ink:#1d1d1d;
    --brand-blue:#1d4f9c;
  }
  *{margin:0;padding:0;box-sizing:border-box}
  html,body{width:1200px;height:1200px;overflow:hidden;background:var(--stage)}
  .flier{position:absolute;left:215px;top:38px;width:783px;height:1098px;background:var(--paper);overflow:hidden;box-shadow:0 6px 18px rgba(0,0,0,.45)}
  .shapes{position:absolute;inset:0;width:783px;height:1098px}
  .brand{position:absolute;left:24px;top:0;width:282px;height:182px}
  .brand-name{position:absolute;left:104px;top:46px;font-family:"Cinzel",serif;font-weight:600;font-size:42px;color:var(--brand-blue);letter-spacing:1px}
  .brand-tag{position:absolute;left:108px;top:98px;font-family:"Cinzel",serif;font-weight:600;font-size:16px;color:var(--brand-blue)}
  .brand-dot{position:absolute;left:40px;top:52px;width:52px;height:52px;border-radius:50%;background:var(--brand-blue)}
  .headline{position:absolute;left:29px;top:456px;font-family:"Cinzel",serif;font-weight:600;font-size:37px;color:#fff;letter-spacing:.5px;white-space:nowrap}
  .service-title{position:absolute;left:29px;top:547px;font-family:"Cinzel",serif;font-weight:600;font-size:31px;color:#fff;letter-spacing:.5px}
  .highlights{position:absolute;left:36px;top:594px;list-style:none;font-family:"Lato",sans-serif;font-size:18px;color:#fff}
  .highlights li{height:31px;line-height:31px;padding-left:16px;position:relative}
  .highlights li::before{content:"";position:absolute;left:0;top:13px;width:7px;height:7px;border-radius:50%;background:#fff}
  .services-title{position:absolute;left:29px;top:730px;font-family:"Cinzel",serif;font-weight:600;font-size:32px;color:var(--blue)}
  .service-list{position:absolute;list-style:none;font-family:"Lato",sans-serif;font-size:16px;color:var(--ink)}
  .service-list li{height:30.5px;display:flex;align-items:center;gap:8px}
  .service-list svg{width:22px;height:20px;flex:none}
  .col-a{left:40px;top:774px}
  .col-b{left:240px;top:776px}
  .about{position:absolute;left:27px;top:880px;width:510px;font-family:"Lato",sans-serif;font-size:15.5px;line-height:19px;color:var(--ink)}
  .about strong{display:block;color:var(--blue);font-weight:700;margin-top:4px}
  .cta{position:absolute;left:32px;top:979px;font-family:"Cinzel",serif;font-weight:600;font-size:21px;color:#fff;letter-spacing:.5px}
  .phone{position:absolute;left:38px;top:1022px;display:flex;align-items:center;gap:12px;font-family:"Cinzel",serif;font-weight:400;font-size:34px;color:var(--brand-blue)}
  .phone svg{width:40px;height:40px}
</style>
</head>
<body>
<div class="flier">
  <svg class="shapes" viewBox="0 0 783 1098" aria-hidden="false">
    <defs>
      <linearGradient id="photoKitchen" x1="0" y1="0" x2="1" y2="1">
        <stop offset="0" stop-color="#f1ede8"/><stop offset=".5" stop-color="#c9a98f"/><stop offset="1" stop-color="#e7e5e2"/>
      </linearGradient>
      <linearGradient id="photoWindow" x1="0" y1="0" x2="1" y2="1">
        <stop offset="0" stop-color="#eef0f1"/><stop offset="1" stop-color="#c8ced2"/>
      </linearGradient>
      <linearGradient id="photoSuit" x1="0" y1="0" x2="1" y2="1">
        <stop offset="0" stop-color="#9aa6b0"/><stop offset=".5" stop-color="#e9ecee"/><stop offset="1" stop-color="#6f7f8c"/>
      </linearGradient>
      <linearGradient id="panelBlue" x1="0" y1="0" x2="1" y2="0">
        <stop offset="0" stop-color="#1f6fb8"/><stop offset="1" stop-color="#0f1d3a"/>
      </linearGradient>
    </defs>

    <rect x="0" y="1076" width="783" height="22" fill="var(--orange)"/>

    <g role="img" aria-label="Photo: technician with flashlight spraying along kitchen cabinets while homeowner watches">
      <polygon points="0,0 783,0 783,395 732,444 0,444" fill="url(#photoKitchen)"/>
    </g>
    <g role="img" aria-label="Photo: gloved hand spraying along a window frame">
      <polygon points="667,514 783,402 783,845 598,660 680,580" fill="url(#photoWindow)"/>
    </g>
    <g role="img" aria-label="Photo: worker in protective suit and respirator spraying">
      <polygon points="565,874 689,771 783,846 783,942 673,1026" fill="url(#photoSuit)"/>
    </g>
    <g role="img" aria-label="Photo: second worker in protective suit spraying indoors">
      <polygon points="425,1030 553,912 657,1010 628,1098 510,1098" fill="url(#photoSuit)"/>
    </g>

    <polygon points="429,759 557,634 682,759 557,887" fill="var(--orange)"/>
    <polygon points="783,982 783,1098 660,1098" fill="var(--blue)"/>

    <polygon points="0,444 729,444 659,514 0,514" fill="var(--magenta)"/>
    <polygon points="0,526 651,526 462,715 0,715" fill="url(#panelBlue)"/>
    <line x1="664" y1="526" x2="475" y2="715" stroke="var(--orange)" stroke-width="5"/>
    <polygon points="0,974 473,974 433,1014 0,1014" fill="var(--magenta)"/>

    <polygon points="24,0 306,0 306,122 165,182 24,122" fill="#fff"/>
    <polyline points="24,122 165,182 306,122" fill="none" stroke="var(--orange)" stroke-width="5"/>
  </svg>

  <div class="brand">
    <span class="brand-dot"></span>
    <span class="brand-name">KRV</span>
    <span class="brand-tag">Cleaning Services</span>
  </div>

  <h1 class="headline">YOUR PROPERTY, OUR PRIORITY</h1>

  <h2 class="service-title">PEST CONTROL SERVICE</h2>
  <ul class="highlights">
    <li>European managed</li>
    <li>Monthly - quarterly - annually maintenance contracts</li>
    <li>On call service</li>
  </ul>

  <h2 class="services-title">OUR SERVICES</h2>
  <ul class="service-list col-a">
    <li><svg viewBox="0 0 22 20"><rect x="1" y="4" width="15" height="15" fill="none" stroke="#1f6fb8" stroke-width="2"/><path d="M4 11l4 4L20 2" fill="none" stroke="#1f6fb8" stroke-width="3"/></svg>General Pest Control</li>
    <li><svg viewBox="0 0 22 20"><rect x="1" y="4" width="15" height="15" fill="none" stroke="#1f6fb8" stroke-width="2"/><path d="M4 11l4 4L20 2" fill="none" stroke="#1f6fb8" stroke-width="3"/></svg>Bed Bugs Control</li>
    <li><svg viewBox="0 0 22 20"><rect x="1" y="4" width="15" height="15" fill="none" stroke="#1f6fb8" stroke-width="2"/><path d="M4 11l4 4L20 2" fill="none" stroke="#1f6fb8" stroke-width="3"/></svg>Rat Control</li>
  </ul>
  <ul class="service-list col-b">
    <li><svg viewBox="0 0 22 20"><rect x="1" y="4" width="15" height="15" fill="none" stroke="#1f6fb8" stroke-width="2"/><path d="M4 11l4 4L20 2" fill="none" stroke="#1f6fb8" stroke-width="3"/></svg>Cockroaches Control</li>
    <li><svg viewBox="0 0 22 20"><rect x="1" y="4" width="15" height="15" fill="none" stroke="#1f6fb8" stroke-width="2"/><path d="M4 11l4 4L20 2" fill="none" stroke="#1f6fb8" stroke-width="3"/></svg>Ant Control</li>
  </ul>

  <p class="about">KRV Pest Control is reinventing the pest control service industry in Dubai.
    <strong>This means you get the right Pest Control Workers, with the right tools at the right time!</strong></p>

  <p class="cta">CALL US NOW FOR A FREE ESTIMATE!</p>
  <div class="phone">
    <svg viewBox="0 0 40 40"><circle cx="20" cy="20" r="18" fill="none" stroke="#1d4f9c" stroke-width="2.5"/><path d="M13 11c2-2 4-1 5 1l1 3c0 1-1 2-2 3 1 3 3 5 6 6 1-1 2-2 3-2l3 1c2 1 3 3 1 5-2 2-5 2-8 0-4-2-8-6-10-10-2-3-1-5 1-7z" fill="none" stroke="#1d4f9c" stroke-width="2"/></svg>
    <span>800 BRIGHTLY</span>
  </div>
</div>
</body>
</html>
```